Talvane Companies Business Card Design

We need a new business card for our Private Equity Real Estate Development firm, “Talvane” and our EB-5 regional center “Moorfield Regional Center” on one card. We prefer a design that is simple, elegant, and represents the luxury products we design and build as well as the financial security and stability our successful history has produced. We are an industry leader in our field and 3rd generation family business that has evolved into an institutional quality investment platform. Considered design size is standard business card dimensions (3.5 x 2 inches with an additional 1/8 inch space for design elements or backgrounds that extend beyond the finished size of your piece.

Target Market(s)

• High net worth individuals
• Highly skilled technical workers and physicians in the US seeking investment-based immigration opportunities
• Sophisticated private equity investors
• Intermediary partners include domestic attorneys and investment brokers, as well as international agent networks
• US real estate developers

Industry/Entity Type

Finance

Contact Information for Business Card

(Providing placeholder info for personal information, please design for longer character spaces, longer names and addresses etc..)
• Logo for Talvane
• Logo for Moorfield Regional Center
• Full name: Dorian Talvane
• Job title: CEO
• Email address: dtalvane@talvanecompanies.example
• Cell phone number: +1.555.318.4476
• Office number +1.555.240.6185
• Office address: Quillan Court 5, 4817 Vista Ardell, Elmbrook, OR.
• Website: www.talvanecompanies.example

Font styles to use
Serif
Sans Serif

Colors
ec1f27
ffffff
000000

Requirements
Must have
• • Logo for Talvane
• • Logo for Moorfield Regional Center
• - Use rounded corners
• (See .ai file included for logos)
Nice to have
• • Simple, elegant design
• • Aesthetically compatible with our website design (www.talvanecompanies.example)
• • Color palette including but not limited to white, black, and red (as per logos)
Should not have
• - Not too much red color
• - Do not stack both logos on top of each other

```html
<!DOCTYPE html>
<html lang="en">
<head>
<meta charset="utf-8">
<title>Talvane Companies Business Card</title>
<link rel="stylesheet" href="https://fonts.googleapis.com/css2?family=PT+Serif:wght@400;700&display=swap">
<style>
  :root {
    --stage: #2a2c30;
    --card-white: #ffffff;
    --card-black: #0b0b0c;
    --ink: #1a1a1a;
    --ink-soft: #4a4a4a;
    --logo-grey: #3c3c3e;
    --paper-text: #ffffff;
  }
  * { box-sizing: border-box; margin: 0; padding: 0; }
  html, body { width: 1200px; height: 900px; overflow: hidden; }
  body {
    background: var(--stage);
    font-family: "PT Serif", Georgia, serif;
    position: relative;
  }
  .card {
    position: absolute;
    top: 307px;
    width: 500px;
    height: 286px;
  }
  .card--front { left: 70px; }
  .card--back {
    left: 630px;
    background: radial-gradient(ellipse at 40% 35%, #1d1d1f 0%, var(--card-black) 70%);
    border-radius: 22px;
    display: flex;
    align-items: center;
    justify-content: center;
    gap: 18px;
  }
  .card-shape { position: absolute; inset: 0; }

  .name-banner {
    position: absolute;
    left: 0; top: 34px;
    width: 250px; height: 36px;
    background: var(--ink);
    clip-path: polygon(0 0, 100% 0, 93% 100%, 0 100%);
    color: var(--paper-text);
    font-size: 22px;
    line-height: 36px;
    padding-left: 22px;
    white-space: nowrap;
  }
  .job-title {
    position: absolute;
    left: 22px; top: 78px;
    font-size: 19px;
    color: var(--ink-soft);
  }
  .contact-list {
    position: absolute;
    left: 22px; top: 118px;
    list-style: none;
    font-size: 12px;
    color: var(--ink);
  }
  .contact-list li {
    display: flex;
    align-items: center;
    gap: 10px;
    height: 21px;
    white-space: nowrap;
  }
  .contact-list svg { width: 11px; height: 11px; flex: none; }

  .regional-mark {
    position: absolute;
    right: 26px; top: 92px;
    display: flex;
    align-items: center;
    gap: 10px;
    font-weight: 700;
    font-size: 19px;
    line-height: 1.1;
    color: var(--logo-grey);
    white-space: nowrap;
  }
  .regional-mark .mark-square {
    width: 16px; height: 16px;
    background: var(--logo-grey);
    flex: none;
  }
  .address {
    position: absolute;
    right: 26px; top: 214px;
    text-align: right;
    font-size: 14px;
    line-height: 1.45;
    color: var(--ink);
    white-space: nowrap;
  }

  .brand-square {
    width: 34px; height: 34px;
    background: var(--paper-text);
  }
  .brand-name {
    font-weight: 700;
    font-size: 50px;
    letter-spacing: 1px;
    color: var(--paper-text);
  }
</style>
</head>
<body>

<section class="card card--front" aria-label="Business card front">
  <svg class="card-shape" viewBox="0 0 500 286" aria-hidden="true">
    <path d="M22 0 H478 A22 22 0 0 1 500 22 V252 A22 22 0 0 1 478 274 H285 L275 286 H22 A22 22 0 0 1 0 264 V22 A22 22 0 0 1 22 0 Z" fill="#ffffff"/>
  </svg>

  <div class="name-banner">Dorian Talvane</div>
  <div class="job-title">CEO</div>

  <div class="regional-mark">
    <span class="mark-square" aria-hidden="true"></span>
    <span>Moorfield<br>Regional Center</span>
  </div>

  <ul class="contact-list">
    <li>
      <svg viewBox="0 0 12 12"><rect x="3" y="0.5" width="6" height="11" rx="1" fill="none" stroke="#1a1a1a"/><rect x="5" y="9.5" width="2" height="1" fill="#1a1a1a"/></svg>
      +1.555.318.4476
    </li>
    <li>
      <svg viewBox="0 0 12 12"><path d="M1 4 Q6 0 11 4 L10 6 L8 5 V4 Q6 3 4 4 V5 L2 6 Z" fill="#1a1a1a"/><rect x="2.5" y="6.5" width="7" height="4.5" rx="1" fill="#1a1a1a"/></svg>
      +1.555.240.6185
    </li>
    <li>
      <svg viewBox="0 0 12 12"><rect x="0.5" y="2.5" width="11" height="7" fill="#1a1a1a"/><path d="M0.5 2.5 L6 7 L11.5 2.5" fill="none" stroke="#fff"/></svg>
      dtalvane@talvanecompanies.example
    </li>
    <li>
      <svg viewBox="0 0 12 12"><circle cx="6" cy="6" r="5.3" fill="#1a1a1a"/><path d="M0.7 6 H11.3 M6 0.7 V11.3 M6 0.7 Q2.5 6 6 11.3 M6 0.7 Q9.5 6 6 11.3" fill="none" stroke="#fff" stroke-width="0.7"/></svg>
      www.talvanecompanies.example
    </li>
  </ul>

  <p class="address">Quillan Court 5, 4817<br>Vista Ardell, Elmbrook, OR</p>
</section>

<section class="card card--back" aria-label="Business card back">
  <span class="brand-square" aria-hidden="true"></span>
  <span class="brand-name">TALVANE</span>
</section>

</body>
</html>
```